stationary for home builder
Birchwood Custom Homes, Inc.
Project: stationary for home builder
stationary for home builder - Real Estate
Creative Brief
Professional
Dale Morrow
President
4200 Tern Avenue, suite 310 Seacliff Bay, CA 90417
bchdalemorrow@mailvista.test

```html
<!DOCTYPE html>
<html lang="en">
<head>
<meta charset="utf-8">
<title>Birchwood Custom Homes, Inc. – Business Card</title>
<link href="https://fonts.googleapis.com/css2?family=Cinzel:wght@400;600;700&display=swap" rel="stylesheet">
<style>
  :root {
    --brand-red: #c0261f;
    --brand-red-dark: #8f1512;
    --brand-red-light: #d9473c;
    --band-grey: #b9b9b9;
    --band-grey-light: #e2e2e2;
    --card-white: #ffffff;
    --ink: #4a4a4a;
    --page: #ececec;
  }
  * { box-sizing: border-box; margin: 0; padding: 0; }
  html, body {
    width: 1200px; height: 980px; overflow: hidden;
    background: var(--page);
    font-family: "Cinzel", serif;
  }
  .sheet {
    width: 1200px; height: 980px;
    display: flex; flex-direction: column;
    align-items: center; justify-content: space-evenly;
  }
  .card {
    position: relative;
    width: 800px; height: 457px;
    border-radius: 22px;
    overflow: hidden;
    box-shadow: 0 6px 18px rgba(0,0,0,.18);
  }

  /* Front */
  .card-front { background: var(--card-white); }
  .card-front .swoosh { position: absolute; inset: 0; width: 100%; height: 100%; }
  .brand {
    position: absolute; left: 44px; top: 92px;
    display: flex; align-items: center; gap: 14px;
    color: var(--brand-red); font-weight: 600;
  }
  .brand-mark { width: 34px; height: 34px; background: var(--brand-red); }
  .brand-name { line-height: 1; }
  .brand-name .main { display: block; font-size: 44px; letter-spacing: 1px; }
  .brand-name .sub { display: block; font-size: 17px; letter-spacing: 1.5px; margin-top: 6px; }

  .contact {
    position: absolute; left: 44px; top: 200px;
    list-style: none;
    font-size: 14px; color: var(--ink); letter-spacing: .6px;
  }
  .contact li { display: flex; align-items: center; gap: 10px; height: 23px; }
  .contact .dot {
    width: 12px; height: 12px; border-radius: 50%;
    background: var(--brand-red); flex: none;
  }

  .person {
    position: absolute; right: 44px; bottom: 38px;
    text-align: right; color: var(--brand-red);
  }
  .person .name { font-size: 24px; font-weight: 600; letter-spacing: 1px; }
  .person .title { font-size: 14px; color: var(--ink); letter-spacing: 1.5px; margin-top: 2px; }

  /* Back */
  .card-back {
    background: linear-gradient(135deg, var(--brand-red-light) 0%, var(--brand-red) 45%, var(--brand-red-dark) 100%);
  }
  .web {
    position: absolute; left: 48px; top: 58px;
    font-size: 22px; letter-spacing: 2px;
    color: rgba(255,255,255,.85);
  }
</style>
</head>
<body>
<main class="sheet">
  <section class="card card-front" aria-label="Card front">
    <svg class="swoosh" viewBox="0 0 800 457" preserveAspectRatio="none" aria-hidden="true">
      <path d="M0,0 H800 V340 C700,190 500,74 0,52 Z" fill="var(--band-grey)"/>
      <path d="M0,0 H800 V318 C700,172 500,60 0,40 Z" fill="var(--band-grey-light)"/>
      <path d="M0,0 H800 V300 C700,158 500,48 0,30 Z" fill="var(--brand-red)"/>
    </svg>

    <div class="brand">
      <span class="brand-mark"></span>
      <span class="brand-name">
        <span class="main">Birchwood</span>
        <span class="sub">Custom Homes, Inc.</span>
      </span>
    </div>

    <ul class="contact">
      <li><span class="dot"></span>4200 Tern Avenue, suite 310</li>
      <li><span class="dot"></span>Seacliff Bay, CA 90417</li>
      <li><span class="dot"></span>949.555.0142</li>
      <li><span class="dot"></span>949.555.0187</li>
      <li><span class="dot"></span>bchdalemorrow@mailvista.test</li>
      <li><span class="dot"></span>www.BirchwoodHomes.test</li>
    </ul>

    <div class="person">
      <div class="name">Dale Morrow</div>
      <div class="title">President</div>
    </div>
  </section>

  <section class="card card-back" aria-label="Card back">
    <div class="web">www.BirchwoodHomes.test</div>
  </section>
</main>
</body>
</html>
```